Stationery for use with Vellmar reports

I would like to get a stationery design that my firm -- Vellmar Partners -- will use as a format for reports that we send our clients. I am specifically looking for a design for use on a piece of paper or letterhead -- not business cards or envelopes.

We are an Africa based US risk intelligence and strategy firm that works with multinational corporations operating in West Africa. Our initial thinking is that we would like a color scheme consistent with our existing logo -- however we are open to other color schemes.

Also, we would like to see at least two separate versions: one with our company name and logo, the other without name and logo.

We also would like font recommendations for the stationary design.

The final design should communicate discreet professionalism and a modern approach, but it should not overshadow the words and information printed on the stationery.

Target Market(s)

Multinational corporations that currently use our products.

Font styles to use
Serif
Sans Serif

Requirements
Must have
• Sense of discreet professionalism that will not overshadow the content we put onto the stationery format.
• We would like to see designs with and without our company name/logo.
• Please suggest fonts that would work with the stationery.
Nice to have
• Ideally colors consistent with out existing logo, though we are open to and even encourage other ideas.
Should not have
• No need for business cards or envelopes.

```html
<!DOCTYPE html>
<html lang="en">
<head>
<meta charset="utf-8">
<title>Vellmar Partners – Letterhead</title>
<link href="https://fonts.googleapis.com/css2?family=Lato:wght@400;800&display=swap" rel="stylesheet">
<style>
  :root {
    --navy: #264c5f;
    --gold: #e6b95a;
    --paper: #ffffff;
    --backdrop: #d6cbc8;
    --ink: #4a4a4a;
  }
  * { margin: 0; padding: 0; box-sizing: border-box; }
  html, body {
    width: 1200px; height: 784px; overflow: hidden;
    background: var(--backdrop);
    font-family: "Lato", sans-serif;
  }
  .letterhead {
    position: absolute; left: 340px; top: 56px;
    width: 520px; height: 672px;
    background: var(--paper);
    box-shadow: 0 4px 14px rgba(0,0,0,0.12);
  }
  .side-band {
    position: absolute; left: 0; top: 0;
    width: 16px; height: 672px;
  }
  .brand {
    position: absolute; left: 50px; top: 48px;
    display: flex; align-items: center; gap: 10px;
  }
  .brand-dot {
    width: 22px; height: 22px; border-radius: 50%;
    background: var(--gold);
  }
  .brand-name {
    font-weight: 800; font-size: 20px; color: var(--navy);
    letter-spacing: 0.5px;
  }
  .contact-tab {
    position: absolute; left: 16px; top: 538px;
    width: 26px; height: 104px;
    background: var(--navy);
  }
  .contact-tab svg { display: block; }
  .contact-list {
    position: absolute; left: 52px; top: 541px;
    list-style: none;
    font-size: 11px; line-height: 15px; color: var(--ink);
  }
  .contact-list li.gap { margin-top: 11px; }
</style>
</head>
<body>
  <main class="letterhead">
    <svg class="side-band" viewBox="0 0 16 672" aria-hidden="true">
      <polygon points="0,0 16,0 16,146 0,152" fill="var(--gold)"/>
      <polygon points="0,158 16,152 16,672 0,672" fill="var(--navy)"/>
    </svg>

    <div class="brand">
      <span class="brand-dot"></span>
      <span class="brand-name">Vellmar Partners</span>
    </div>

    <div class="contact-tab">
      <svg width="26" height="104" viewBox="0 0 26 104" aria-hidden="true">
        <rect x="3.5" y="26" width="19" height="75" fill="none" stroke="#fff" stroke-width="1.2"/>
        <!-- pin -->
        <path d="M13 4.5a4 4 0 0 1 4 4c0 3-4 7-4 7s-4-4-4-7a4 4 0 0 1 4-4z" fill="#fff"/>
        <circle cx="13" cy="8.5" r="1.5" fill="var(--navy)"/>
        <!-- phone -->
        <path d="M9.5 35.5c1-1 2-1 2.5 0l.8 1.4c.3.6 0 1-.5 1.3 .6 1.3 1.5 2.2 2.8 2.8.3-.5.7-.8 1.3-.5l1.4.8c1 .5 1 1.5 0 2.5-3 2-10-4.5-8.3-8.3z" fill="#fff"/>
        <!-- mail -->
        <rect x="8" y="56" width="10" height="7" fill="#fff"/>
        <path d="M8 56l5 4 5-4" fill="none" stroke="var(--navy)" stroke-width="1"/>
        <!-- globe -->
        <circle cx="13" cy="86" r="5" fill="#fff"/>
        <path d="M8 86h10M13 81v10M13 81c-2.5 3-2.5 7 0 10M13 81c2.5 3 2.5 7 0 10" fill="none" stroke="var(--navy)" stroke-width="0.7"/>
      </svg>
    </div>

    <ul class="contact-list">
      <li>418 Harbour View Road</li>
      <li>Suite 7, Ridge District</li>
      <li class="gap">(555) 014-2290</li>
      <li>info@vellmarpartners.com</li>
      <li>www.vellmarpartners.com</li>
    </ul>
  </main>
</body>
</html>
```